Logo + Business Card Design Project

We are looking at changing our logo and reprinting business cards.

Attached is a design concept for the logo (we have no hi res files for this).

The logo needs to be able to work standalone without the tagline.

We are happy for you to use this concept or design a new one. The existing concept is quite well liked.

We would also consider not having Solutions in the logo and just have QRV Systems Pty Ltd in the body text of the card.

We have a Tag Line that needs to go on all documentation / websites etc wherever the logo appears.

Tagline: Turning IT up

Our message to clients is that we have solutions that:

QRV Systems:
Turning IT up

Turning up Revenue
Turning up Profit
Turning up Confidence

We would require the files in a High Res format for print and a scalable transparent format for web.
(We also need greyscale and monochrome files)
All source files need to be delivered with existing layers etc

A corporate guide with the logo usage and colours should be specified.

Suggestions:
The new logo has to have CMYK colours of 100 90 0 0

CMYK 100 90 0 0
RGB #21409A
Websafe #224499
Greyscale #414141

We would also need a business card layout designed.
Could be one sided or 2 sided. Will probably print matt cello 2 sides on 350gsm gloss
Updates

Industry/Entity Type

Business

Requirements
Should not have
• Lower case n in QRV.

```html
<!DOCTYPE html>
<html lang="en">
<head>
<meta charset="utf-8">
<title>QRV Systems – Logo and Business Card</title>
<link rel="stylesheet" href="https://fonts.googleapis.com/css2?family=PT+Sans:ital,wght@0,400;0,700;1,400&family=Roboto+Condensed:wght@400;700&display=swap">
<style>
  :root {
    --brand-blue: #21409a;
    --brand-blue-mid: #3a55a8;
    --accent-sky: #b8cad8;
    --band-grey: #c9d2e4;
    --text-dark: #1f1f1f;
    --text-grey: #4a4a4a;
    --rule-grey: #b5b5b5;
    --frame-grey: #c8c8c8;
    --paper: #ffffff;
  }
  * { margin: 0; padding: 0; box-sizing: border-box; }
  html, body {
    width: 1200px; height: 509px; overflow: hidden;
    background: var(--paper);
  }
  .sheet { position: relative; width: 1200px; height: 509px; }

  /* Logo lockup: name with one plain square */
  .logo { display: flex; align-items: center; }
  .logo-square { flex: none; background: var(--accent-sky); }
  .logo-name {
    font-family: "PT Sans", sans-serif; font-weight: 700;
    color: var(--brand-blue); line-height: 1; white-space: nowrap;
  }

  .logo-standalone { position: absolute; left: 6px; top: 215px; gap: 14px; }
  .logo-standalone .logo-square { width: 56px; height: 56px; }
  .logo-standalone .logo-name { font-size: 60px; }

  /* Business card */
  .card {
    position: absolute; left: 436px; top: 3px; width: 762px; height: 504px;
    border: 1px solid var(--frame-grey); background: var(--paper); overflow: hidden;
  }
  .card-logo { position: absolute; left: 20px; top: 60px; gap: 8px; }
  .card-logo .logo-square { width: 30px; height: 30px; }
  .card-logo .logo-name { font-size: 34px; }

  .holder {
    position: absolute; right: 20px; top: 34px; text-align: right;
    font-family: "PT Sans", sans-serif;
  }
  .holder-name { color: var(--brand-blue); font-size: 37px; line-height: 1.1; }
  .holder-title { color: var(--text-grey); font-size: 28px; font-style: italic; line-height: 1.15; }

  .rule { position: absolute; height: 1px; background: var(--rule-grey); }
  .rule-dot {
    position: absolute; width: 14px; height: 14px; border-radius: 50%;
    background: var(--brand-blue); margin: -7px 0 0 -7px;
  }
  .rule-top { left: 439px; right: 0; top: 122px; }
  .rule-top-dot { left: 439px; top: 122px; }
  .rule-mid { left: 0; right: 0; top: 394px; }
  .rule-mid-dot { left: 323px; top: 394px; }

  .contact {
    position: absolute; left: 0; right: 0; text-align: center;
    font-family: "Roboto Condensed", sans-serif; color: var(--text-grey);
  }
  .contact .sep { color: var(--text-dark); font-weight: 700; padding: 0 4px; }
  .contact-phones { top: 318px; font-size: 26px; line-height: 30px; }
  .contact-web { top: 404px; font-size: 23px; line-height: 28px; color: var(--text-dark); }

  .bands { position: absolute; left: 0; right: 0; bottom: 0; }
  .band-light { background: var(--band-grey); height: 10px; }
  .band-white { background: var(--paper); height: 4px; }
  .band-mid { background: var(--brand-blue-mid); height: 8px; opacity: 0.55; }
  .band-deep { background: var(--brand-blue); height: 8px; }
</style>
</head>
<body>
<div class="sheet">

  <div class="logo logo-standalone">
    <span class="logo-square" aria-hidden="true"></span>
    <span class="logo-name">QRV Systems</span>
  </div>

  <section class="card" aria-label="Business card">
    <div class="logo card-logo">
      <span class="logo-square" aria-hidden="true"></span>
      <span class="logo-name">QRV Systems</span>
    </div>

    <div class="holder">
      <p class="holder-name">Daniel Ashcombe</p>
      <p class="holder-title">Project Director</p>
    </div>

    <div class="rule rule-top"></div>
    <span class="rule-dot rule-top-dot"></span>

    <div class="contact contact-phones">
      <p>Phone: + 61 29555-0140<span class="sep">|</span>Support: + 61 29555-0177</p>
      <p>Fax : + 61 29555-0141<span class="sep">|</span>Mobile : 0400 555 218</p>
    </div>

    <div class="rule rule-mid"></div>
    <span class="rule-dot rule-mid-dot"></span>

    <div class="contact contact-web">
      <p>Email: daniel.ashcombe@qrv.com.au<span class="sep">|</span>Web: www.qrv.com.au</p>
      <p>Address : 117/45 Harwood Lane Northbridge NSW 2063</p>
    </div>

    <div class="bands" aria-hidden="true">
      <div class="band-light"></div>
      <div class="band-white"></div>
      <div class="band-mid"></div>
      <div class="band-deep"></div>
    </div>
  </section>

</div>
</body>
</html>
```